Charged by courts for driving with suspended license

To be seen by judges and lawyers. Would like some consistency between the brochures which is why we have used same images in places.

Target Market(s)

Lawyers, judges

Industry/Entity Type

legal, auto

Font styles to use
Sans Serif

Requirements
Nice to have
• I like the gears graphic I have used, but open to other ideas. Should be less industrial/automotive rather reflect mentally Turning Point as clients need to change driving behaviour
Should not have
• images with manufacturers names etc. Maybe not have bright colours that are fun or summery as this si for judges, legal profession and must be serious, professional and stately

```html
<!DOCTYPE html>
<html lang="en">
<head>
<meta charset="utf-8">
<title>Turning Point – Suspended Licence Course</title>
<link href="https://fonts.googleapis.com/css2?family=Oswald:wght@600;700&family=Roboto+Condensed:wght@400&family=Montserrat:wght@500;600;700&display=swap" rel="stylesheet">
<style>
  :root {
    --navy-deep: #1b2940;
    --navy-panel: #3a4e6a;
    --slate-blue: #5e8196;
    --slate-light: #6a8da1;
    --white: #ffffff;
    --ink: #1b2940;
  }
  * { margin: 0; padding: 0; box-sizing: border-box; }
  html, body { width: 1200px; height: 853px; overflow: hidden; background: var(--navy-deep); }
  .brochure { position: relative; width: 1200px; height: 853px; overflow: hidden; font-family: "Roboto Condensed", "Arial Narrow", sans-serif; color: var(--white); }

  .content-panel { position: absolute; left: 0; top: 0; width: 799px; height: 853px; background: var(--navy-deep); }
  .decor-gears { position: absolute; left: 250px; top: 20px; width: 540px; height: 833px;
    background: radial-gradient(ellipse at 40% 20%, rgba(10,18,32,.75), rgba(10,18,32,0) 60%),
                linear-gradient(170deg, rgba(18,29,48,0) 40%, rgba(18,29,48,.7) 75%, rgba(18,29,48,0) 100%); }

  .title { position: absolute; left: 52px; top: 24px; font-family: "Oswald", sans-serif; font-weight: 700; line-height: .98; letter-spacing: -.6px; white-space: nowrap; }
  .title .kicker { display: block; color: var(--slate-blue); font-size: 35px; padding-left: 4px; }
  .title .main { display: block; color: var(--white); font-size: 44px; }

  .column { position: absolute; }
  .col-left { left: 51px; top: 114px; width: 290px; }
  .col-mid { left: 454px; top: 66px; width: 292px; }
  .section-head { font-family: "Oswald", sans-serif; font-weight: 600; color: var(--slate-blue); font-size: 19.5px; line-height: 1.02; margin-bottom: 5px; letter-spacing: -.4px; }
  .section { margin-bottom: 20px; }
  .lead { font-size: 17px; line-height: 1; margin-bottom: 6px; }
  .item { font-size: 17px; line-height: 1.0; text-indent: 17px; margin-bottom: 6px; }

  .side-panel { position: absolute; left: 799px; top: 0; width: 401px; height: 853px; background: var(--navy-panel); }
  .side-curve { position: absolute; left: 0; top: 0; }
  .remote-icon { position: absolute; left: 838px; top: 58px; width: 124px; height: 124px; border-radius: 14px; background: linear-gradient(160deg, #6f90a3, #56788d); }
  .remote-head { position: absolute; left: 972px; top: 88px; font-family: "Oswald", sans-serif; font-weight: 700; line-height: .98; white-space: nowrap; }
  .remote-head .a { display: block; color: var(--slate-blue); font-size: 39px; padding-left: 13px; }
  .remote-head .b { display: block; color: var(--white); font-size: 41px; }
  .illustration { position: absolute; left: 826px; top: 208px; width: 340px; height: 192px; border-radius: 60px 12px 12px 60px; background: linear-gradient(135deg, #e8ecf0, #c9d3dd 60%, #8fa3bd); }

  .cost-pill { position: absolute; left: 834px; top: 411px; width: 259px; height: 40px; background: var(--white); border-radius: 6px; display: flex; align-items: center; padding: 0 5px; font-family: "Montserrat", sans-serif; white-space: nowrap; }
  .cost-label { background: var(--slate-blue); color: var(--white); font-weight: 600; font-size: 13.5px; padding: 6px 6px; border-radius: 6px; }
  .cost-value { color: var(--ink); font-weight: 700; font-size: 19px; margin-left: 9px; }

  .one-on-one { position: absolute; left: 897px; top: 515px; width: 280px; text-align: center; font-family: "Oswald", sans-serif; font-weight: 700; font-size: 37px; line-height: 1; color: var(--white); }

  .school-name { position: absolute; left: 852px; top: 608px; width: 284px; text-align: center; font-family: "Montserrat", sans-serif; font-weight: 600; color: var(--ink); white-space: nowrap; }
  .school-name .big { display: block; font-size: 50px; line-height: 1.4; letter-spacing: -1px; }
  .school-name .small { display: block; font-size: 20.5px; letter-spacing: .6px; margin-top: 0; }
  .tagline { position: absolute; left: 852px; top: 742px; width: 284px; text-align: center; font-family: "Montserrat", sans-serif; font-weight: 500; color: var(--navy-panel); font-size: 15.5px; letter-spacing: .2px; white-space: nowrap; }
  .programs { position: absolute; left: 852px; top: 767px; width: 284px; display: flex; justify-content: space-between; font-family: "Montserrat", sans-serif; font-weight: 500; color: var(--navy-panel); font-size: 12.5px; white-space: nowrap; }
</style>
</head>
<body>
<main class="brochure">
  <section class="content-panel">
    <div class="decor-gears" role="img" aria-label="Faint interlocking gears and a winding road as background decoration"></div>

    <h1 class="title"><span class="kicker">SUSPENDED LICENCE</span><span class="main">TURNING POINT</span></h1>

    <div class="column col-left">
      <div class="section">
        <h2 class="section-head">During the course we will:</h2>
        <p class="lead">Defensive Driving module (The Big 4):</p>
        <p class="item">I. Lane position (better to drop 2 wheels on the shoulder than hit an oncoming vehicle)</p>
        <p class="item">II. Following distance (varies depending on speed and conditions); space cushion driving (always have an out)</p>
        <p class="item">III. Defensive stopping (what should we do every time we apply brakes?)</p>
        <p class="item">IV. Strategic driving / what we do with our eyes:</p>
      </div>
      <div class="section">
        <h2 class="section-head">Law:</h2>
        <p class="item">I. Highway Traffic Act (privilege vs right); Federal &amp; Provincial; ways we can lose our license</p>
        <p class="item">II. Implications of a criminal record (relationships, work, financial)</p>
      </div>
      <div class="section">
        <h2 class="section-head">Road Rage:</h2>
        <p class="item">I. Defining the continuum of road rage and escalation of anger</p>
        <p class="item">II. Triggers</p>
        <p class="item">III. Personality types (Type A); Holmes &amp; Rahe stress scale</p>
        <p class="item">IV. Aggressive driving (overlap between aggressors and victims); reframing our views</p>
        <p class="item">V. Psychiatric issues/PTSD:&nbsp; Not uncommon to have professional drivers come through the course due to over-exposure to stress from driving (both on the job and/or the commute to their driving job)</p>
      </div>
    </div>

    <div class="column col-mid">
      <div class="section">
        <h2 class="section-head">Physiology of aggressive driving<br>and how it affects the body:</h2>
        <p class="item">I. Window of tolerance (hyper-arousal vs hypo-arousal)</p>
        <p class="item">II. Fight or flight response:&nbsp; how it works</p>
        <p class="item">III. Stress hormones (Adrenaline, Cortisol, Norepinephrine)</p>
        <p class="item">IV. Chronic levels of exposure/Immune system suppression</p>
        <p class="item">V. Hypertension</p>
        <p class="item">VI. Sympathetic nervous system</p>
        <p class="item">VII. Substances - will do an overview of alcohol/drinking and driving if relevant; individual and general factors that contribute to B.A.C</p>
      </div>
      <div class="section">
        <h2 class="section-head">Personal context (risk vs protective factors); incumbent upon us to consider:</h2>
        <p class="item">I. Genetics (chemical predispositions)</p>
        <p class="item">II. Socialization (role models)</p>
        <p class="item">III. Environment</p>
      </div>
      <div class="section">
        <h2 class="section-head">Strategies to manage:</h2>
        <p class="item">I. Stages of change theory; habit formation and how to reprogram (many of our decisions on any day are subconscious i.e., no decision-making process)</p>
        <p class="item">II. Neuroplasticity and habit formation</p>
        <p class="item">III. Supernormal stimuli:&nbsp; how our bodies have not kept up to the complexities of today’s society and its stresses</p>
        <p class="item">IV. Ensure cerebral part of brain is making decisions and not “lizard” part of brain (amygdala vs cerebrum and their roles in the body); triggers &amp; stressors</p>
      </div>
    </div>
  </section>

  <aside class="side-panel">
    <svg class="side-curve" width="401" height="853" viewBox="0 0 401 853" aria-hidden="true">
      <path d="M0 620 C 90 520, 230 470, 401 463 L 401 853 L 0 853 Z" fill="var(--slate-light)"/>
    </svg>
  </aside>

  <div class="remote-icon" role="img" aria-label="Icon of a computer monitor with a person and a chat bubble"></div>
  <h2 class="remote-head"><span class="a">OFFERED</span><span class="b">REMOTELY!</span></h2>
  <div class="illustration" role="img" aria-label="Illustration of an instructor presenting an online lesson with video, certificate and graduation icons"></div>

  <div class="cost-pill"><span class="cost-label">Course Cost:</span><span class="cost-value">$775.00 + HST</span></div>

  <h2 class="one-on-one">COURSES ARE<br>ONE-ON-ONE</h2>

  <div class="school-name"><span class="big">Steadyway</span><span class="small">DRIVING SCHOOL</span></div>
  <p class="tagline">CAREFUL HABITS ON EVERY ROAD</p>
  <p class="programs"><span>•BEGGINER</span><span>•REHABILITATION</span><span>•REMEDIAL</span></p>
</main>
</body>
</html>
```